Revamp a website that sells books on machine learning and A.I

Hello I would like to create a minimalist concept to revamp this website:

www.quillorbit.co.uk

We can change everything including the logo.

Somethings that I don't like:
- Generic images of people.
- Robot images.

The books are about the mathematics for machine learning and A.I and I would like for the website to have a blog as well as a scheduling tool, were people can book a call with me.

The scheduling tool, needs to have text and different tiers, for example 15 m free and 60 m 45 usd

Target Market(s)

university students and mathematics enthusiasts

Industry/Entity Type

machine learning, education, books, mathematics, A.I

Number of Pages Required

4 page

Requirements
Must have
• Landing Page, blog page, scheduling page, optimised conversion funnel
Should not have
• Arbitrary images from people or robots

```html
<!DOCTYPE html>
<html lang="en">
<head>
<meta charset="utf-8">
<title>QuillOrbit – Mathematics for Machine Learning</title>
<link href="https://fonts.googleapis.com/css2?family=Lexend:wght@400;600;700;800&family=Roboto:ital,wght@0,400;0,500;0,700;1,400&display=swap" rel="stylesheet">
<style>
:root{
  --blue:#1e8bf5;
  --cyan:#19b6f0;
  --cyan-soft:#8fd8f6;
  --navy:#071a36;
  --ink:#141414;
  --text:#555b66;
  --band:#eaf4fe;
  --footer:#333333;
  --white:#ffffff;
  --line:#c9ccd2;
}
*{box-sizing:border-box;margin:0;padding:0}
html,body{width:1200px;height:3750px;overflow:hidden;background:var(--white)}
body{font-family:"Roboto",sans-serif;color:var(--ink)}
.page{position:relative;width:1200px;height:3750px;overflow:hidden}
.abs{position:absolute}
.decor{position:absolute;left:0;top:0;width:1200px;height:3750px;pointer-events:none}

/* header */
.brand{left:145px;top:36px;display:flex;align-items:center;gap:10px;font-family:"Lexend",sans-serif;font-weight:700;font-size:30px;color:var(--blue);letter-spacing:.5px}
.brand-mark{width:34px;height:34px;border-radius:50%;background:var(--cyan)}
.nav{left:456px;top:45px;display:flex;gap:0;font-size:14px;font-weight:500;text-transform:uppercase}
.nav a{color:var(--ink);text-decoration:none;margin-right:30px}
.nav a.active{border-left:3px solid var(--cyan);padding-left:6px}
.cart{left:893px;top:40px}
.btn{display:inline-flex;align-items:center;justify-content:center;border-radius:24px;background:linear-gradient(90deg,var(--cyan),var(--blue));color:var(--white);font-weight:700;font-size:14px;text-transform:uppercase;text-decoration:none}
.login{left:940px;top:32px;width:114px;height:44px;gap:8px}

/* hero */
.hero-title{left:0;width:1200px;top:332px;text-align:center;font-family:"Lexend",sans-serif;font-weight:700;font-size:62px;color:var(--white);letter-spacing:-1px}
.hero-title span{color:var(--cyan)}
.hero-sub{left:0;width:1200px;top:425px;text-align:center;font-size:19px;font-weight:500;color:var(--white)}
.hero-cta{left:523px;top:475px;width:154px;height:42px;background:var(--blue)}

/* schedule */
.schedule{left:191px;top:859px;width:367px;height:444px;background:var(--white);box-shadow:0 8px 30px rgba(0,0,0,.08);border-top:4px solid var(--blue)}
.schedule h2{font-family:"Lexend",sans-serif;font-size:27px;font-weight:700;text-align:center;margin-top:36px}
.tick{display:block;width:26px;height:3px;background:var(--cyan);margin:10px auto 0;border-radius:2px}
.field{position:absolute;border:1.5px solid #a9adb4;border-radius:24px;font-size:11px;color:#333;padding:0 24px;display:flex;align-items:center}
.tiers{position:absolute;left:34px;top:226px;font-size:11px;display:flex;align-items:center;gap:10px}
.tiers strong{font-size:13px;font-weight:500}
.radio{width:15px;height:15px;border:1.5px solid #777;border-radius:50%;display:inline-block;vertical-align:middle;margin-right:4px}
.tiers a{color:var(--blue)}
.submit{position:absolute;left:114px;top:367px;width:136px;height:44px}

.about-kicker{left:638px;top:940px;font-family:"Lexend",sans-serif;font-weight:700;font-size:25px;color:var(--cyan)}
.about-name{left:638px;top:974px;font-family:"Lexend",sans-serif;font-weight:700;font-size:38px;letter-spacing:-.5px}
.about-rule{left:638px;top:1030px;width:24px;height:3px;background:var(--cyan)}
.about-lead{left:638px;top:1052px;font-size:19px}
.about-text{left:638px;top:1092px;width:418px;font-size:13px;line-height:25px;color:var(--text);text-align:justify}
.about-btn{left:638px;top:1235px;width:135px;height:45px}

/* section headings */
.kicker{left:0;width:1200px;text-align:center;font-family:"Lexend",sans-serif;font-weight:700;font-size:24px;color:var(--cyan)}
.heading{left:0;width:1200px;text-align:center;font-family:"Lexend",sans-serif;font-weight:700;font-size:40px;letter-spacing:-.5px}
.rule{left:588px;width:24px;height:3px;background:var(--cyan)}

/* products */
.product{background:var(--white);border:2px solid #dde3ea;border-radius:120px;width:446px;height:238px}
.product.featured{border:2px solid var(--cyan);box-shadow:0 8px 18px rgba(30,139,245,.25)}
.cover{position:absolute;left:46px;top:36px;width:108px;height:162px;background:linear-gradient(160deg,#f2b64c,#e89a2a)}
.product-info{position:absolute;left:183px;top:28px;width:230px}
.product-title{font-size:18px;line-height:24px}
.price{font-size:18px;color:var(--cyan);margin-top:4px}
.cart-btn{width:130px;height:42px;margin-top:12px;font-size:13px}
.toc{display:block;margin-top:10px;font-size:13px;font-weight:700;color:var(--blue);text-decoration:underline;text-transform:uppercase}
.arrow{width:44px;height:44px;border-radius:50%;border:1.5px solid #888;background:var(--white);display:flex;align-items:center;justify-content:center}

/* blog */
.post{width:277px;height:186px;border:2px solid #d6d9de;background:var(--white)}
.post.featured{box-shadow:0 6px 16px rgba(0,0,0,.15)}
.date{position:absolute;left:20px;top:20px;width:46px;height:46px;background:var(--blue);color:var(--white);text-align:center;font-size:20px;font-weight:700;line-height:22px;padding-top:3px}
.date small{display:block;font-size:12px;font-weight:500;line-height:14px}
.post-title{position:absolute;left:80px;top:20px;width:180px;font-size:16px;font-weight:500;line-height:23px}
.post-text{position:absolute;left:20px;top:86px;width:240px;font-size:12px;line-height:19px;color:#9a9ea5}
.post-more{position:absolute;left:20px;top:152px;font-size:13px;font-weight:700;color:var(--blue)}

/* release */
.release-kicker{color:#9fe3ff}
.release-title{left:511px;top:2650px;font-family:"Lexend",sans-serif;font-weight:600;font-size:24px;color:var(--white)}
.release-tag{left:511px;top:2694px;width:550px;font-size:18px;line-height:24px;color:#8fd8ff}
.release-text{left:514px;top:2750px;width:540px;font-size:14px;line-height:25px;color:var(--white)}
.release-btn{left:511px;top:2864px;width:156px;height:44px;background:transparent;border:2px solid var(--white);font-size:13px}

/* reviews */
.review{left:223px;top:3232px;width:754px;height:219px;background:var(--white);box-shadow:0 6px 24px rgba(0,0,0,.08)}
.review-bar{left:275px;top:3451px;width:651px;height:8px;background:var(--cyan)}
.quote-mark{position:absolute;left:0;width:754px;top:30px;text-align:center;font-family:"Lexend",sans-serif;font-size:46px;font-weight:800;color:var(--cyan);font-style:italic;line-height:40px}
.quote{position:absolute;left:80px;width:594px;top:80px;text-align:center;font-size:16px;line-height:26px;font-style:italic;color:#333}
.reviewer{position:absolute;left:0;width:754px;top:172px;text-align:center;font-size:18px;color:var(--cyan);font-weight:500}

/* footer */
.footer{left:0;top:3411px;width:1200px;height:339px;background:var(--footer)}
.foot-h{top:3530px;color:var(--white);font-size:22px;font-weight:500}
.foot-divider{top:3521px;width:1px;height:128px;background:#666}
.email{left:144px;top:3588px;width:221px;height:41px;background:var(--white);font-size:13px;color:#333;padding:13px 18px}
.subscribe{left:365px;top:3588px;width:105px;height:41px;background:var(--blue);color:var(--white);font-weight:700;font-size:14px;display:flex;align-items:center;justify-content:center}
.social{left:584px;top:3586px;display:flex;gap:12px}
.social span{width:34px;height:34px;border-radius:50%;border:2px solid var(--white)}
.links{top:3580px;font-size:13px;line-height:26px;color:var(--white)}
.copyright{left:0;width:1200px;top:3696px;text-align:center;font-size:13px;color:var(--white)}
</style>
</head>
<body>
<div class="page">

<svg class="decor" viewBox="0 0 1200 3750" aria-hidden="true">
  <defs>
    <linearGradient id="heroGrad" x1="0" y1="0" x2="1" y2="1">
      <stop offset="0" stop-color="#06152e"/><stop offset=".55" stop-color="#0b2a55"/><stop offset="1" stop-color="#0d5f8e"/>
    </linearGradient>
    <radialGradient id="glowGrad"><stop offset="0" stop-color="#2bd0ff"/><stop offset="1" stop-color="#04254a"/></radialGradient>
  </defs>
  <!-- soft blue highlight behind hero -->
  <circle cx="430" cy="240" r="100" fill="#dff4ff"/>
  <circle cx="1200" cy="870" r="140" fill="#e6f5fe"/>
  <!-- outline rings -->
  <g fill="none" stroke="#8fd8f6" stroke-width="1.5">
    <circle cx="20" cy="390" r="100"/>
    <circle cx="1210" cy="830" r="110"/>
    <circle cx="150" cy="1120" r="190"/>
    <circle cx="140" cy="1120" r="175"/>
    <circle cx="1130" cy="1430" r="75"/><circle cx="1130" cy="1430" r="60"/>
    <circle cx="0" cy="1740" r="70"/>
    <circle cx="580" cy="2470" r="140"/>
    <circle cx="30" cy="3150" r="120"/><circle cx="30" cy="3150" r="100"/>
    <circle cx="1180" cy="3150" r="75"/><circle cx="1180" cy="3150" r="60"/>
  </g>
  <!-- hero image area -->
  <g role="img" aria-label="Photo of glowing blue data streams flowing from hands typing on a laptop">
    <path fill="url(#heroGrad)" d="M0,230 C0,160 90,140 190,142 C300,145 380,190 500,190 C570,190 600,150 640,125 C730,80 850,90 960,130 C1130,190 1215,330 1200,520 C1185,710 1030,830 860,828 C700,826 590,760 520,660 C470,590 430,540 330,520 C250,505 160,520 90,470 C30,430 0,350 0,230 Z"/>
    <circle cx="860" cy="330" r="120" fill="#1aa8d8" opacity=".35"/>
  </g>
  <g fill="#ffffff"><circle cx="715" cy="744" r="4" fill="#19b6f0"/><circle cx="736" cy="744" r="4"/><circle cx="757" cy="744" r="4"/></g>
  <circle cx="297" cy="616" r="68" fill="url(#glowGrad)" role="img" aria-label="Photo of a glowing circuit board"/>
  <!-- schedule photo circles -->
  <circle cx="186" cy="873" r="70" fill="url(#glowGrad)" role="img" aria-label="Photo of a glowing blue neural pattern"/>
  <circle cx="373" cy="862" r="96" fill="url(#glowGrad)" role="img" aria-label="Photo of blue light streaks over a dark background"/>
  <circle cx="195" cy="1140" r="115" fill="#0b5f99" role="img" aria-label="Photo of a digital interface in deep blue"/>
  <!-- featured band -->
  <path fill="#eaf4fe" d="M0,1369 H1050 A273,273 0 0 1 1050,1915 H0 Z"/>
  <rect x="0" y="1369" width="260" height="546" fill="#dde9f4" role="img" aria-label="Faint pattern of scattered numbers"/>
  <!-- release band -->
  <path fill="#1e8bf5" d="M150,2410 H1050 A150,150 0 0 1 1200,2560 V2850 A154,154 0 0 1 1046,3004 H180 C60,3004 0,2950 0,2860 V2560 A150,150 0 0 1 150,2410 Z"/>
  <circle cx="150" cy="2760" r="320" fill="#1478e6" opacity=".55"/>
  <circle cx="0" cy="2910" r="30" fill="#1478e6"/>
</svg>

<!-- header -->
<div class="abs brand"><span class="brand-mark"></span>QUILLORBIT</div>
<nav class="abs nav">
  <a class="active" href="#">Home</a><a href="#">About Us</a><a href="#">Books</a><a href="#">Blog</a><a href="#">Contact Us</a>
</nav>
<svg class="abs cart" width="28" height="28" viewBox="0 0 28 28" aria-label="Cart">
  <path d="M2 4h4l3 13h13l3-9H8" fill="none" stroke="#141414" stroke-width="2.2" stroke-linejoin="round"/>
  <circle cx="11" cy="22" r="2" fill="#141414"/><circle cx="20" cy="22" r="2" fill="#141414"/>
  <circle cx="22" cy="5" r="4" fill="#19b6f0"/>
</svg>
<a class="abs btn login" href="#">
  <svg width="14" height="14" viewBox="0 0 14 14"><circle cx="7" cy="4" r="3" fill="none" stroke="#fff" stroke-width="1.5"/><path d="M1 13c0-4 12-4 12 0" fill="none" stroke="#fff" stroke-width="1.5"/></svg>Login
</a>

<!-- hero -->
<h1 class="abs hero-title"><span>MACHINE</span> LEARNING</h1>
<p class="abs hero-sub">Sed ut perspiciatis unde omnis iste natus</p>
<a class="abs btn hero-cta" href="#">Get Started</a>

<!-- schedule -->
<section class="abs schedule">
  <h2>SCHEDULE NOW</h2><span class="tick"></span>
  <div class="field" style="left:25px;top:110px;width:152px;height:44px">Enter Name</div>
  <div class="field" style="left:186px;top:110px;width:154px;height:44px">Enter Email</div>
  <div class="field" style="left:25px;top:166px;width:315px;height:44px">Phone</div>
  <div class="tiers"><strong>Scheduling time</strong><span><i class="radio"></i>15 m <a href="#">FREE</a></span><span><i class="radio"></i>60 m <a href="#">45 USD</a></span></div>
  <div class="field" style="left:25px;top:262px;width:315px;height:84px;align-items:flex-start;padding-top:16px;border-radius:20px">Message</div>
  <a class="btn submit" href="#">Submit</a>
</section>

<div class="abs about-kicker">ABOUT</div>
<h2 class="abs about-name">TOMAS VERANO</h2>
<div class="abs about-rule"></div>
<p class="abs about-lead">A Mathematician and now a book writer</p>
<p class="abs about-text">I am a mathematician with over a decade of experience in developing and deploying machine learning systems. My books are written in an conversational style with humour. They are rich in practical applications, enabling readers to not only grasp the concepts but also understand their real-world applications in the field of Data Science.</p>
<a class="abs btn about-btn" href="#">Read More</a>

<!-- featured -->
<div class="abs kicker" style="top:1452px">OUR</div>
<h2 class="abs heading" style="top:1482px">FEATURED PRODUCTS</h2>
<div class="abs rule" style="top:1540px"></div>

<div class="abs arrow" style="left:84px;top:1689px"><svg width="14" height="18"><path d="M10 2 3 9l7 7" fill="none" stroke="#555" stroke-width="2"/></svg></div>
<div class="abs arrow" style="left:1070px;top:1689px"><svg width="14" height="18"><path d="M4 2l7 7-7 7" fill="none" stroke="#555" stroke-width="2"/></svg></div>

<article class="abs product featured" style="left:146px;top:1591px">
  <div class="cover" role="img" aria-label="Book cover, volume 2 on calculus, with an illustrated robot and bees"></div>
  <div class="product-info">
    <div class="product-title">Ahead of Inference Vol 2 - Calculus EBOOK PDF</div>
    <div class="price">7,50 €</div>
    <a class="btn cart-btn" href="#">Add to Cart</a>
    <a class="toc" href="#">Table of Contents</a>
  </div>
</article>
<article class="abs product" style="left:609px;top:1591px">
  <div class="cover" role="img" aria-label="Book cover, volume 1 on linear algebra, with an illustrated robot"></div>
  <div class="product-info">
    <div class="product-title">Ahead of Inference Vol 1 - Linear Algebra EBOOK PDF</div>
    <div class="price">7,50 €</div>
    <a class="btn cart-btn" href="#">Add to Cart</a>
    <a class="toc" href="#">Table of Contents</a>
  </div>
</article>

<!-- blog -->
<div class="abs kicker" style="top:2006px">OUR</div>
<h2 class="abs heading" style="top:2036px">FROM THE BLOG</h2>
<div class="abs rule" style="top:2096px"></div>

<div class="abs arrow" style="left:84px;top:2210px"><svg width="14" height="18"><path d="M10 2 3 9l7 7" fill="none" stroke="#555" stroke-width="2"/></svg></div>
<div class="abs arrow" style="left:1070px;top:2210px"><svg width="14" height="18"><path d="M4 2l7 7-7 7" fill="none" stroke="#555" stroke-width="2"/></svg></div>

<article class="abs post" style="left:156px;top:2140px">
  <div class="date">02<small>JAN</small></div>
  <div class="post-title">Pellentesque faucibus Ut accumsan ultric</div>
  <p class="post-text">Duis quam Nam eget lacus Aliquam erat volutpat Quisque dignissim congue leovel lacus vitae felis vestibulum</p>
  <a class="post-more">READ MORE</a>
</article>
<article class="abs post featured" style="left:462px;top:2140px">
  <div class="date">02<small>JAN</small></div>
  <div class="post-title">Pellentesque faucibus Ut accumsan ultric</div>
  <p class="post-text">Duis quam Nam eget lacus Aliquam erat volutpat Quisque dignissim congue leovel lacus vitae felis vestibulum</p>
  <a class="post-more">READ MORE</a>
</article>
<article class="abs post" style="left:767px;top:2140px">
  <div class="date">02<small>JAN</small></div>
  <div class="post-title">Pellentesque faucibus Ut accumsan ultric</div>
  <p class="post-text">Duis quam Nam eget lacus Aliquam erat volutpat Quisque dignissim congue leovel lacus vitae felis vestibulum</p>
  <a class="post-more">READ MORE</a>
</article>

<!-- latest release -->
<div class="abs kicker release-kicker" style="top:2476px">OUR</div>
<h2 class="abs heading" style="top:2506px;color:#fff">LATEST RELEASE</h2>
<div class="abs rule" style="top:2566px;background:#fff"></div>
<div class="abs" style="left:183px;top:2580px;width:238px;height:360px;background:linear-gradient(160deg,#f2b64c,#e4962a);box-shadow:4px 6px 14px rgba(0,0,0,.25)" role="img" aria-label="Book cover, volume 2 on calculus, with an illustrated robot and bees"></div>
<h3 class="abs release-title">Ahead of Inference Vol 2 - Calculus</h3>
<p class="abs release-tag">Embark on a buzzing exploration of calculus in machine learning, where bees are your companions in deciphering the secrets of AI.</p>
<p class="abs release-text">Calculus is essential in machine learning and algorithm optimization, offering tools for function analysis and model tuning. Key concepts like derivatives and integrals are crucial for optimizing neural networks and minimizing error rates, making a strong understanding of calculus vital for success in these advanced fields.</p>
<a class="abs btn release-btn" href="#">Start Reading</a>

<!-- reviews -->
<div class="abs kicker" style="top:3083px">OUR</div>
<h2 class="abs heading" style="top:3112px">CUSTOMER'S REVIEWS</h2>
<div class="abs rule" style="top:3172px"></div>

<div class="abs arrow" style="left:144px;top:3318px"><svg width="14" height="18"><path d="M10 2 3 9l7 7" fill="none" stroke="#555" stroke-width="2"/></svg></div>
<div class="abs arrow" style="left:1010px;top:3318px"><svg width="14" height="18"><path d="M4 2l7 7-7 7" fill="none" stroke="#555" stroke-width="2"/></svg></div>

<!-- footer -->
<footer class="abs footer"></footer>
<div class="abs review-bar"></div>
<section class="abs review">
  <div class="quote-mark">“</div>
  <p class="quote">"...The conversational tone of the book is its biggest strength. It feels less like a traditional textbook and more like a novel. This approach makes the reader feel at ease, particularly when tackling complex topics... "</p>
  <div class="reviewer">Rina</div>
</section>

<div class="abs foot-h" style="left:144px">Subscribe for a free chapter!</div>
<div class="abs foot-divider" style="left:539px"></div>
<div class="abs foot-h" style="left:584px">Social Media</div>
<div class="abs foot-divider" style="left:843px"></div>
<div class="abs foot-h" style="left:893px">Links</div>
<div class="abs email">Enter Email</div>
<div class="abs subscribe">SUBSCRIBE</div>
<div class="abs social" aria-label="Social media links"><span></span><span></span><span></span><span></span><span></span></div>
<div class="abs links" style="left:894px">Home<br>About Us<br>Books</div>
<div class="abs links" style="left:989px">Blog<br>Contact Us</div>
<p class="abs copyright">Copyright © 2024 All rights reserved by Quillorbit &nbsp;|&nbsp; Privacy Policy &nbsp;|&nbsp; Terms of Use</p>

</div>
</body>
</html>
```